Survey & Inspection Van Wrap - 2023 Halvik Cargo Van 250

We would like our van to pop! We want everyone to know that this van is for survey and inspection. The phrase "We are utility specialists." needs to be on the van. And the words "Design. Inspect. Protect." The van will be wrapped in black so the font of the words need to be white. Also, our website www.torvane.ca and our email inforequest@torvane.ca needs to be on it.

Target Market(s)

Hydro-Electricity Companies, Telecom Companies, Natural Gas companies

Industry/Entity Type

Telecom, Utilities, Municipal Water, Natural Gas, etc.

Font styles to use
Other font styles liked:
• Glacial Indifference

Requirements
Must have
• must have our logo and the phrase "We are utility specialists" and "Design. Inspect. Protect."
Nice to have
• Large scale. Modern. Professional. Engineering Grade
Should not have
• Should not be in any colours that aren't contained within our logo already

```html
<!DOCTYPE html>
<html lang="en">
<head>
<meta charset="utf-8">
<title>Torvane Utility Services – Van Wrap Concepts</title>
<link rel="stylesheet" href="https://fonts.googleapis.com/css2?family=Open+Sans:wght@400;600&family=Poppins:wght@400;600&family=Oswald:wght@400&display=swap">
<style>
  :root {
    --wrap-black: #0b0b0b;
    --wrap-orange: #d98a1f;
    --stripe-orange: #c98516;
    --text-white: #f2f2f2;
    --text-dark: #111111;
    --glass: #cfd0d1;
    --trim: #1c1c1c;
    --tire: #202020;
    --rim: #8a8a8a;
    --hub: #5a5a5a;
    --taillight: #b3141c;
    --page: #ffffff;
  }
  html, body {
    margin: 0;
    padding: 0;
    width: 1200px;
    height: 1200px;
    overflow: hidden;
    background: var(--page);
  }
  .wrap-sheet { display: block; width: 1200px; height: 1200px; }
  .brand-name { font-family: "Open Sans", sans-serif; font-weight: 600; fill: var(--text-white); letter-spacing: 3px; }
  .brand-sub { font-family: "Open Sans", sans-serif; font-weight: 400; fill: var(--wrap-orange); }
  .tagline { font-family: "Poppins", sans-serif; font-weight: 400; letter-spacing: 2px; }
  .tagline-accent { font-weight: 600; fill: var(--wrap-orange); }
  .tagline-on-stripe { fill: var(--text-dark); }
  .tagline-on-stripe .tagline-accent { fill: var(--text-white); }
  .tagline-on-black { fill: var(--text-white); letter-spacing: 1px; }
  .motto { font-family: "Oswald", sans-serif; fill: var(--text-white); letter-spacing: 2.5px; }
  .website { font-family: "Poppins", sans-serif; fill: var(--text-dark); letter-spacing: 0.5px; }
  .website-bold { font-weight: 600; }
  .email { font-family: "Poppins", sans-serif; font-weight: 400; letter-spacing: 0.3px; }
  .email-on-black { fill: var(--text-white); }
  .email-on-orange { fill: var(--text-dark); }
  .body-black { fill: var(--wrap-black); }
  .body-orange { fill: var(--wrap-orange); }
  .stripe { fill: var(--stripe-orange); }
  .glass { fill: var(--glass); }
  .trim { fill: var(--trim); }
  .taillight { fill: var(--taillight); }
  .tire { fill: var(--tire); }
  .rim { fill: var(--rim); }
  .hub { fill: var(--hub); }
  .brand-square { fill: var(--wrap-orange); }
  .brand-square-outline { fill: var(--wrap-black); stroke: var(--wrap-orange); stroke-width: 8; }
</style>
</head>
<body>
<svg class="wrap-sheet" viewBox="0 0 966 966" xmlns="http://www.w3.org/2000/svg">
  <defs>
    <path id="van-body" d="M160,340 L162,190 Q165,150 200,150 L590,150 Q640,152 680,190 L720,235 Q790,250 815,268 Q835,285 835,320 L835,345 Q835,362 815,362 L160,362 Z"/>
    <clipPath id="van-body-clip"><use href="#van-body"/></clipPath>
    <g id="van-hardware">
      <path class="glass" d="M578,168 L655,168 Q688,178 703,228 L703,246 L578,246 Z"/>
      <path class="trim" d="M158,312 L838,318 L838,350 Q836,364 815,364 L158,364 Z"/>
      <rect class="taillight" x="166" y="228" width="16" height="76" rx="3"/>
      <path class="trim" d="M245,362 A62,62 0 0 1 365,362 Z"/>
      <path class="trim" d="M655,362 A62,62 0 0 1 775,362 Z"/>
      <circle class="tire" cx="305" cy="360" r="46"/>
      <circle class="rim" cx="305" cy="360" r="26"/>
      <circle class="hub" cx="305" cy="360" r="9"/>
      <circle class="tire" cx="715" cy="360" r="46"/>
      <circle class="rim" cx="715" cy="360" r="26"/>
      <circle class="hub" cx="715" cy="360" r="9"/>
    </g>
  </defs>

  <!-- Concept A: full black wrap with orange belt stripe -->
  <g class="concept concept-black">
    <use href="#van-body" class="body-black"/>
    <path class="stripe" d="M168,252 L822,262 L824,290 L168,284 Z" clip-path="url(#van-body-clip)"/>
    <use href="#van-hardware"/>

    <rect class="brand-square" x="204" y="166" width="62" height="62" rx="8"/>
    <text class="brand-name" x="288" y="220" font-size="42">TORVANE</text>
    <text class="brand-sub" x="306" y="246" font-size="22">Utility Services Ltd.</text>
    <text class="tagline tagline-on-stripe" x="248" y="274" font-size="12">We are <tspan class="tagline-accent">utility specialists</tspan></text>
    <text class="motto" x="298" y="296" font-size="12">DESIGN. INSPECT. PROTECT.</text>
    <text class="website" x="566" y="276" font-size="12">www.<tspan class="website-bold">torvane</tspan>.ca</text>
    <text class="email email-on-black" x="566" y="303" font-size="10">inforequest@torvane.ca</text>
  </g>

  <!-- Concept B: black rear with orange cab -->
  <g class="concept concept-split" transform="translate(0,385)">
    <use href="#van-body" class="body-orange"/>
    <g clip-path="url(#van-body-clip)">
      <rect class="body-black" x="150" y="140" width="330" height="230"/>
      <rect class="body-black" x="378" y="142" width="170" height="178" rx="24"/>
    </g>
    <use href="#van-hardware"/>

    <rect class="brand-square-outline" x="396" y="166" width="128" height="128" rx="18"/>

    <text class="tagline tagline-on-black" x="197" y="174" font-size="11">We are <tspan class="tagline-accent">utility specialists</tspan></text>
    <text class="brand-name" x="180" y="217" font-size="30">TORVANE</text>
    <text class="brand-sub" x="188" y="238" font-size="19">Utility Services Ltd.</text>
    <text class="motto" x="197" y="272" font-size="11">DESIGN. INSPECT. PROTECT.</text>
    <text class="website" x="562" y="280" font-size="12">www.<tspan class="website-bold">torvane</tspan>.ca</text>
    <text class="email email-on-orange" x="562" y="297" font-size="10">inforequest@torvane.ca</text>
  </g>
</svg>
</body>
</html>
```